Harbor Lantern Productions Business Logo and Card Design

PLEASE LIMIT your submission to maximum of 2 at a time.
Harbor Lantern Productions provides video production services, and produces videos, that help people connect in the spirit of unity and peace.Primarily I am looking for a logo that is simple to remember but the concept is fairly complex. The concept of the logo is a peace dove with an olive branch in it's mouth has it's wings around earth, symbolising that it is protecting earth with peace. If possible I'd like this logo done and delivered in high quality vector format, so I can use it for banners etc.Then the business card I just want a simple white card with the logo in the middle and contact info under the logo. Open to suggestions if you think there should be anything else included, but it must remain simple and uncluttered. Also incorporate something in the logo that says film and video e.g.: film strip or camera lens

Contact Information for Business Card

Harbor Lantern Productions
www.harborlantern.example
teodor@harborlantern.example
+61 478 315 064

Requirements
Must have
• Logo must have the following:
• Peace Dove
• Olive branch
• Earth
• Something about video production (e.g.: film strip or camera lens or anything film related)

```html
<!DOCTYPE html>
<html lang="en">
<head>
<meta charset="utf-8">
<title>Harbor Lantern Productions — Business Card</title>
<link rel="stylesheet" href="https://fonts.googleapis.com/css2?family=Old+Standard+TT:wght@400&display=swap">
<style>
  :root {
    --card-bg: #ffffff;
    --frame-outer: #2f7bf0;
    --frame-inner: #4cc94c;
    --contact-band: #98f58f;
    --ink: #1a1a1a;
    --brand-dot: #35c3f5;
  }
  * { margin: 0; padding: 0; box-sizing: border-box; }
  html, body {
    width: 1200px;
    height: 741px;
    overflow: hidden;
    background: var(--card-bg);
  }
  .card {
    position: relative;
    width: 1200px;
    height: 741px;
    background: var(--card-bg);
    font-family: "Old Standard TT", "Times New Roman", serif;
    color: var(--ink);
  }
  .card-frames {
    position: absolute;
    inset: 0;
  }
  .brand-lockup {
    position: absolute;
    left: 0;
    right: 0;
    top: 320px;
    display: flex;
    align-items: center;
    justify-content: center;
    gap: 22px;
  }
  .brand-dot {
    width: 64px;
    height: 64px;
    border-radius: 50%;
    background: var(--brand-dot);
    flex: none;
  }
  .brand-name {
    font-size: 54px;
    font-weight: 400;
    line-height: 1;
    color: var(--ink);
    white-space: nowrap;
  }
  .contact-line {
    position: absolute;
    left: 110px;
    right: 68px;
    top: 640px;
    display: flex;
    justify-content: space-between;
    font-size: 27px;
    line-height: 1;
    white-space: nowrap;
    color: var(--ink);
  }
</style>
</head>
<body>
  <main class="card">
    <svg class="card-frames" width="1200" height="741" viewBox="0 0 1200 741" aria-hidden="true">
      <rect class="contact-band" x="19" y="615" width="1160" height="92" fill="var(--contact-band)"/>
      <rect class="frame-inner" x="44" y="44" width="1113" height="650" fill="none" stroke="var(--frame-inner)" stroke-width="4" rx="3"/>
      <rect class="frame-outer" x="19" y="19" width="1160" height="700" fill="none" stroke="var(--frame-outer)" stroke-width="4" rx="3"/>
    </svg>

    <div class="brand-lockup">
      <span class="brand-dot" aria-hidden="true"></span>
      <span class="brand-name">Harbor Lantern Productions</span>
    </div>

    <p class="contact-line">
      <span class="contact-web">www.harborlantern.example</span>
      <span class="contact-email">teodor@harborlantern.example</span>
      <span class="contact-phone">+61 478 315 064</span>
    </p>
  </main>
</body>
</html>
```